Comedy Hypnosis Fundraiser Show

I am a Comedy Hypnotist and need a poster designed for an upcoming Comedy Hypnosis Show Fundraiser. I will be doing the show for an organization called, Liras Teal Boxes of Cheer. I need a design that will help increase interest and ticket sales. We do have a sponsor and their logo which I've uploaded, MUST appear someplace on the poster and be large enough for people to see that they have sponsored the show. I am not to picky on the design or colors. Just need something that will draw an audience while highlighting the purpose of the show.

About Liras Teal Boxes of Cheer: Lira is 12 years old and about a year ago she wanted to brighten patients days who are receiving chemo. She has been using her own tooth fairy money to buy goodies for the bags. She does this ALL on her own. Every item put in the bags are hand picked by her. Since then, she has begun to get many donations and has embarked on a remarkable adventure. Her goal is to go to as many hospitals as possible all over the country and help as many as she can!

About Me The Hypnotist: Imagine all the fun & laughter you’ll enjoy during the Dorian Falque Comedy Hypnosis Show…Now DOUBLE that GOOD-TIME FEELING and as you continue reading, you’re going to discover the most powerful comedy hypnotist of all time!

The second Dorian steps on stage, his hypnotic shows are filled with outrageous entertainment as he transforms members of the audience into the start of the show. He uses breath-taking displays of hypnotic phenomena, unbelievable energy and hysterical comedy to weave a truly unforgettable and high-octane show.

Combining his quick-wit, loveable charm and powerful hypnotic ability, this dynamic entertainer brings this old-age mystical art form kicking and screaming into the 21st century leaving your guests talking (and laughing) until next year when you feel compelled to hire him again.

Dorian is an awe-inspiring comedy hypnotist, but he’s also a dynamic entertainer and energetic perform who can get the very best out of every single on stage opportunity. Dorian’s show keeps audiences on the edge of their seats and often rolling in the aisles.

This laugh out loud, high caliber, Las Vegas style show has mystified audiences at high schools, colleges, comedy clubs, and casinos across the country. A hit with corporations and event planners, if you want to secure this rock-star performer for your event, you better do it months in advance.

When you’re ready to hire a comedy hypnotist to dazzle your audience in a hilarious, action packed, Las Vegas style show there is only one name you need to know, DORIAN FALQUE.

Target Market(s)

This show poster must capture an audience from High School aged as posters will be in the High School and also the general public of all ages.

Requirements
Must have
• 1) There must be a logo of our show sponsor which I have uploaded, and their business name The Quill Motor Company.
• 3) The poster must be a typical size of 11X17 inches.
• 2) There must be a photo of me on the poster, but it doesn't have to be large. Just enough to add some mystery to the show. I have uploaded images of me, but they need to be made transparent as they have a green background right now.
• 3) The poster must have the following information: Mention the show is a Comedy Hypnosis fundraiser for Lira's Teal Boxes of Cheer. My name some-place on the poster as "Award-Winning Comedy Hypnotist Dorian Falque"
• 4) Basic Show information below must be someplace on poster.
• Location: WD Ostrand High School
• Date: December 14th, 2013
• Show Time: 7:00pm
• Ticket Price: $10 Advance / $12 at the door
• Tickets can be purchased online at www.dorianfalque.example or by calling 715-382-9107
Nice to have
• I've already marketed the show as "Get Hypnotized, Mesmerized, or Otherwise for Liras Teal Boxes of Cheer" So this might be a creative way mentioned her cause.
• As her color is PINK a show poster that incorporates some excellent colors of Pink might be perfect to draw in some attention.

```html
<!DOCTYPE html>
<html lang="en">
<head>
<meta charset="utf-8">
<title>Dorian Falque – The Comedy Hypnotist</title>
<link rel="stylesheet" href="https://fonts.googleapis.com/css2?family=Anton&family=Oswald:wght@500;700&family=Kaushan+Script&display=swap">
<style>
  :root {
    --black: #050505;
    --white: #ffffff;
    --pink: #e23cc8;
    --pink-light: #f47ee6;
    --pink-deep: #a3158f;
    --gold-top: #ffe15a;
    --gold-bottom: #f08a12;
    --yellow: #ffe629;
    --ink: #111111;
    --sponsor-blue: #1c5fae;
  }
  * { box-sizing: border-box; margin: 0; padding: 0; }
  html, body { width: 778px; height: 1200px; overflow: hidden; background: var(--white); }
  .poster {
    position: relative;
    width: 778px;
    height: 1200px;
    background: linear-gradient(180deg, var(--pink-light), var(--pink) 60%, var(--pink-light));
    padding: 14px;
    font-family: "Oswald", sans-serif;
  }
  .header {
    height: 200px;
    background: var(--black);
    text-align: center;
    color: var(--white);
  }
  .date {
    font-family: "Anton", sans-serif;
    font-size: 50px;
    letter-spacing: 2px;
    line-height: 68px;
    padding-top: 4px;
  }
  .performer {
    font-family: "Anton", sans-serif;
    font-weight: 400;
    font-size: 82px;
    line-height: 86px;
    letter-spacing: 1px;
    background: linear-gradient(180deg, var(--gold-top), var(--gold-bottom));
    -webkit-background-clip: text;
    background-clip: text;
    color: transparent;
  }
  .tagline {
    font-weight: 700;
    font-size: 34px;
    line-height: 36px;
    letter-spacing: 2px;
  }
  .stage {
    position: relative;
    height: 560px;
    background: radial-gradient(circle at 45% 50%, var(--pink-light) 0%, var(--pink) 45%, var(--pink-deep) 100%);
    overflow: hidden;
  }
  .hypnotist-photo {
    position: absolute;
    left: 70px;
    top: 40px;
    width: 400px;
    height: 520px;
    border-radius: 200px 200px 0 0;
    background: linear-gradient(180deg, #c9a58c 0%, #9a7a66 45%, #3b2f2b 100%);
    opacity: 0.85;
  }
  .stage-copy {
    position: absolute;
    right: 30px;
    top: 60px;
    width: 270px;
    display: flex;
    flex-direction: column;
    align-items: center;
    text-align: center;
  }
  .showtime {
    font-family: "Kaushan Script", cursive;
    color: var(--yellow);
    font-size: 40px;
    line-height: 46px;
    text-shadow: 2px 2px 0 var(--black);
  }
  .cause-lead {
    margin-top: 40px;
    font-weight: 700;
    font-size: 20px;
    line-height: 23px;
    color: var(--white);
    text-shadow: 1px 1px 0 var(--black);
  }
  .cause-name {
    margin-top: 10px;
    font-family: "Kaushan Script", cursive;
    font-size: 38px;
    line-height: 44px;
    color: var(--black);
  }
  .cause-name .accent { color: var(--white); text-shadow: 2px 2px 0 var(--black); }
  .venue {
    height: 128px;
    background: var(--black);
    text-align: center;
    padding-top: 8px;
  }
  .venue-name {
    font-family: "Anton", sans-serif;
    color: var(--yellow);
    font-size: 42px;
    line-height: 46px;
    letter-spacing: 2px;
  }
  .venue-address {
    font-weight: 700;
    color: var(--white);
    font-size: 22px;
    line-height: 28px;
  }
  .tickets {
    padding-top: 16px;
    text-align: center;
    color: var(--ink);
  }
  .sponsor {
    display: inline-flex;
    align-items: center;
    gap: 24px;
    background: var(--white);
    padding: 10px 34px;
    height: 68px;
  }
  .sponsor-label {
    font-family: "Kaushan Script", cursive;
    font-size: 36px;
    color: var(--sponsor-blue);
  }
  .sponsor-name {
    display: flex;
    align-items: center;
    gap: 10px;
    font-weight: 700;
    font-size: 30px;
    color: var(--ink);
  }
  .sponsor-mark { width: 26px; height: 26px; background: var(--sponsor-blue); }
  .ticket-lead {
    margin-top: 12px;
    font-weight: 700;
    font-size: 26px;
    line-height: 30px;
  }
  .ticket-site {
    font-family: "Anton", sans-serif;
    font-size: 52px;
    line-height: 58px;
  }
  .ticket-phone, .ticket-price {
    font-weight: 700;
    font-size: 24px;
    line-height: 29px;
  }
</style>
</head>
<body>
  <main class="poster">
    <header class="header">
      <p class="date">SATURDAY 12/14/13</p>
      <h1 class="performer">DORIAN FALQUE</h1>
      <p class="tagline">THE COMEDY HYPNOTIST</p>
    </header>

    <section class="stage">
      <div class="hypnotist-photo" role="img" aria-label="Photo of the hypnotist holding both hands toward the viewer in front of a pink hypnotic swirl"></div>
      <div class="stage-copy">
        <p class="showtime">Show Starts<br>at 7pm</p>
        <p class="cause-lead">SHOW TO<br>HELP SUPPORT</p>
        <p class="cause-name"><span class="accent">Lira's</span><br>TEAL BOXES<br><span class="accent">of</span> CHEER</p>
      </div>
    </section>

    <section class="venue">
      <p class="venue-name">W.D. OSTRAND HIGH SCHOOL<br>THEATRE</p>
      <p class="venue-address">2250 WEST HARLAN AVE. MILLBROOK, SD 57010</p>
    </section>

    <section class="tickets">
      <div class="sponsor">
        <span class="sponsor-label">Sponsored by:</span>
        <span class="sponsor-name"><span class="sponsor-mark"></span>Quill Motor Company</span>
      </div>
      <p class="ticket-lead">TICKETS CAN BE PURCHASED ONLINE AT</p>
      <p class="ticket-site">WWW.DORIANFALQUE.EXAMPLE</p>
      <p class="ticket-phone">OR BY CALLING 715-382-9107</p>
      <p class="ticket-price">$10 ADVANCE / $12 AT THE DOOR</p>
    </section>
  </main>
</body>
</html>
```